Design Our Holiday Magic Coupon

Purpose - The purpose of this project is to create a festive, uplifting, and visually engaging physical coupon that will be mailed to our existing community and warm leads.
The intent is twofold: first, to spark delight and connection by offering a tangible, personal touch during the holiday season; and second, to encourage customers to explore and purchase our programs as they prepare for a strong start to 2026. This mailer is designed to re-engage past buyers, inspire current participants, and gently invite new momentum into their practice through a simple, friendly offer.

Project Description + Scope

This project includes the design and production of a printed coupon ( card format) featuring a 20% discount on purchases of $79 or more. The copy should feel warm, clear, and celebratory without urgency or pressure.

The front of the card will include the headline (“Live Your Best 2026”), bold discount information, and the coupon code FESTIVE20. The back will include a short message reinforcing the tone of possibility and ease, plus simple redemption instructions and the expiry date: December 31, 2025. Deliverables include print-ready artwork, color selection aligned with KH brand style.

one side
LIVE YOUR BEST 2026
Enjoy 20% OFF when you buy $79 or more.
Use code: FESTIVE20
Redeem until end of day December 31, 2025.

Back side - Move with clarity.
Heal with intelligence.
Lead with ease.
Thank you for being part of Kinetic Harmony.
Lots of love, Mara and the whole of Team Mara

Target Market(s)

yoga teachers, yoga lovers, mostly over 50 years, women

Font styles to use
Other font styles liked:
• see attached for feel

Colors
0054AA
0677BA
7BADD7
CADEEF
E8F1F8
0094D4
00A9DD
6FCCEA
C7EBF8
E9F6FB
00AB8E
00BBA5
67D7C9
C6EFE9
E9F9F6
EB3D1F
EC4F4E
F09395
F8D3D4
FCEDEE

Requirements
Nice to have
• see attached

```html
<!DOCTYPE html>
<html lang="en">
<head>
<meta charset="utf-8">
<title>Kinetic Harmony – Holiday Coupon</title>
<link rel="stylesheet" href="https://fonts.googleapis.com/css2?family=Playfair+Display:wght@700;900&family=Poppins:wght@300;400;500;600&family=Kaushan+Script&display=swap">
<style>
  :root {
    --stage: #e1e1e1;
    --sky-top: #4b9fd2;
    --sky-mid: #8ad4ee;
    --sky-low: #6fcbea;
    --indigo: #3c3ac9;
    --indigo-deep: #3530a8;
    --pill-text: #4d9fd4;
    --azure: #0a9ff0;
    --azure-deep: #0677ba;
    --navy: #1f2a6b;
    --white: #ffffff;
  }
  * { box-sizing: border-box; margin: 0; padding: 0; }
  html, body { width: 1200px; height: 2246px; overflow: hidden; background: var(--stage); }
  body { position: relative; font-family: "Poppins", sans-serif; }

  .card {
    position: absolute; left: 143px; width: 913px; height: 913px; overflow: hidden;
    background:
      radial-gradient(ellipse 60% 45% at 50% 55%, rgba(160,225,245,.55), transparent 70%),
      linear-gradient(180deg, var(--sky-top) 0%, var(--sky-mid) 45%, var(--sky-low) 80%);
    box-shadow: 0 8px 22px rgba(0,0,0,.28);
  }
  .card--front { top: 147px; }
  .card--back { top: 1184px; }

  .wave-field { position: absolute; top: 150px; width: 200px; height: 600px; opacity: .35;
    background: linear-gradient(180deg, transparent, rgba(255,255,255,.45), transparent); }
  .wave-field--left { left: 0; border-radius: 0 100% 100% 0 / 0 50% 50% 0; }
  .wave-field--right { right: 0; border-radius: 100% 0 0 100% / 50% 0 0 50%; }

  .center { position: absolute; left: 0; right: 0; text-align: center; }

  .brand { position: absolute; top: 62px; left: 0; right: 0; display: flex; justify-content: center; align-items: center; gap: 22px; }
  .brand__dot { width: 58px; height: 58px; border-radius: 50%; background: var(--white); }
  .brand__name { font-family: "Poppins", sans-serif; font-weight: 400; font-size: 42px; line-height: 40px; color: var(--white); letter-spacing: 1px; }

  .pill { background: var(--white); border-radius: 40px; font-family: "Playfair Display", serif; font-weight: 700; color: var(--pill-text); text-align: center; position: absolute; }
  .pill--headline { left: 262px; width: 392px; top: 190px; height: 66px; font-size: 54px; line-height: 66px; }

  .headline-best { top: 262px; font-family: "Playfair Display", serif; font-weight: 900; font-size: 196px; line-height: 180px; color: var(--indigo-deep); letter-spacing: 2px; }
  .headline-year { top: 440px; font-family: "Playfair Display", serif; font-weight: 700; font-size: 128px; line-height: 112px; color: var(--white); }

  .offer-enjoy { position: absolute; left: 90px; top: 598px; width: 164px; height: 44px; background: linear-gradient(90deg, var(--azure), var(--azure-deep)); border-radius: 22px 0 0 22px; color: var(--white); font-family: "Playfair Display", serif; font-size: 36px; line-height: 44px; text-align: center; }
  .offer-value { position: absolute; left: 262px; top: 575px; font-family: "Playfair Display", serif; font-weight: 700; font-size: 122px; line-height: 122px; color: var(--indigo-deep); }
  .offer-percent { position: absolute; left: 385px; top: 572px; font-family: "Playfair Display", serif; font-size: 66px; line-height: 66px; color: var(--white); }
  .offer-off { position: absolute; left: 386px; top: 646px; font-family: "Poppins", sans-serif; font-weight: 600; font-size: 42px; line-height: 42px; color: var(--white); }
  .offer-terms { position: absolute; left: 497px; top: 590px; width: 327px; height: 110px; background: linear-gradient(180deg, var(--azure), var(--azure-deep)); border-radius: 0 55px 55px 0; padding: 9px; }
  .offer-terms__inner { height: 100%; border: 2px dashed var(--white); border-left-width: 2px; border-radius: 0 46px 46px 0; padding: 8px 0 0 28px; color: var(--white); font-weight: 500; font-size: 35px; line-height: 37px; }
  .offer-terms sup { font-size: 18px; vertical-align: 14px; }

  .band { position: absolute; left: 0; right: 0; bottom: 0; background: var(--indigo); }
  .band__edge { position: absolute; left: 0; top: -10px; width: 100%; height: 11px; display: block; }
  .card--front .band { top: 745px; }
  .card--back .band { top: 747px; }

  .coupon-code { position: absolute; left: 134px; top: 51px; width: 305px; height: 63px; background: var(--azure); border-radius: 32px; padding: 6px; }
  .coupon-code__inner { height: 100%; border: 2px dashed var(--white); border-radius: 26px; font-family: "Playfair Display", serif; font-weight: 700; font-size: 26px; line-height: 47px; color: var(--navy); text-align: center; }
  .expiry { position: absolute; left: 458px; top: 52px; font-weight: 600; font-size: 25px; line-height: 28px; color: var(--white); }

  .pill--lead { left: 328px; width: 259px; height: 50px; font-size: 44px; line-height: 50px; }
  .pill--move { top: 54px; }
  .pill--heal { top: 211px; }
  .pill--lead-with { top: 372px; }
  .value-word { font-family: "Playfair Display", serif; font-weight: 900; font-size: 88px; line-height: 80px; color: var(--indigo-deep); }
  .value-word--clarity { top: 120px; }
  .value-word--intelligence { top: 279px; }
  .value-word--ease { top: 440px; }

  .thanks-script { top: 562px; font-family: "Kaushan Script", cursive; font-size: 44px; line-height: 56px; color: var(--indigo-deep); }
  .thanks-line { top: 622px; font-weight: 300; font-size: 35px; line-height: 44px; color: var(--white); }

  .signoff-script { top: 30px; font-family: "Kaushan Script", cursive; font-size: 40px; line-height: 48px; color: var(--white); }
  .signoff-line { top: 82px; font-weight: 400; font-size: 34px; line-height: 40px; color: var(--white); }
</style>
</head>
<body>
<svg width="0" height="0" style="position:absolute">
  <defs>
    <pattern id="zigzag" width="17" height="11" patternUnits="userSpaceOnUse">
      <polygon points="0,11 8.5,0 17,11" fill="#3c3ac9"/>
    </pattern>
  </defs>
</svg>

<section class="card card--front" aria-label="Coupon front">
  <div class="wave-field wave-field--left" role="img" aria-label="Soft flowing line pattern"></div>
  <div class="wave-field wave-field--right" role="img" aria-label="Soft flowing line pattern"></div>

  <div class="brand">
    <span class="brand__dot"></span>
    <span class="brand__name">kinetic<br>harmony</span>
  </div>

  <div class="pill pill--headline">LIVE YOUR</div>
  <h1 class="center headline-best">BEST</h1>
  <div class="center headline-year">2026</div>

  <div class="offer-enjoy">ENJOY</div>
  <div class="offer-value">20</div>
  <div class="offer-percent">%</div>
  <div class="offer-off">OFF</div>
  <div class="offer-terms"><div class="offer-terms__inner">when you buy<br><sup>$</sup>79 or more</div></div>

  <div class="band">
    <svg class="band__edge" preserveAspectRatio="none"><rect width="100%" height="11" fill="url(#zigzag)"/></svg>
    <div class="coupon-code"><div class="coupon-code__inner">Use code: FESTIVE20</div></div>
    <p class="expiry">Redeem until end of day<br>December 31, 2025.</p>
  </div>
</section>

<section class="card card--back" aria-label="Coupon back">
  <div class="wave-field wave-field--left" role="img" aria-label="Soft flowing line pattern"></div>
  <div class="wave-field wave-field--right" role="img" aria-label="Soft flowing line pattern"></div>

  <div class="pill pill--lead pill--move">Move with</div>
  <div class="center value-word value-word--clarity">CLARITY</div>
  <div class="pill pill--lead pill--heal">Heal with</div>
  <div class="center value-word value-word--intelligence">INTELLIGENCE</div>
  <div class="pill pill--lead pill--lead-with">Lead with</div>
  <div class="center value-word value-word--ease">EASE</div>

  <div class="center thanks-script">Thank you</div>
  <p class="center thanks-line">For being part of Kinetic Harmony</p>

  <div class="band">
    <svg class="band__edge" preserveAspectRatio="none"><rect width="100%" height="11" fill="url(#zigzag)"/></svg>
    <div class="center signoff-script">Lots of love,</div>
    <p class="center signoff-line">Mara and the whole of Team Mara</p>
  </div>
</section>
</body>
</html>
```